Tarnwick is a steel frame construction company that builds residential and commercial homes

1. Homepage (we are after a basic website)
Hero Section:
A full-width image or video showcasing steel frames in construction or a finished project.
Tagline: Short, impactful tagline (e.g., "Strong Structures for Tomorrow").
Call-to-Action (CTA): A prominent "Get a Quote" or "Contact Us" button.
About Us (Snapshot Section):

A few lines about the company, emphasizing experience, certifications, and commitment to quality.
Include a "Learn More" button linking to the detailed About Us page.
Products/Services Section:

Feature the main products like steel frames for industrial, residential, and commercial projects.
Each category should have a "Learn More" link to a dedicated product page.
Project Showcase/Portfolio:

Display 2-3 featured projects with images, descriptions, and a "View All Projects" button.
Certifications & Partners:

Display logos of certifications (QSB, local building standards) and partnerships with construction companies or industry bodies.
Footer:

Contact information, quick links (Home, About, Products, Services, Contact), and social media icons.
2. Products Page
Overview:

A grid or list layout showing different steel frame products or services.
Each product should have a title, brief description, and a thumbnail image.
Individual Product Pages:

Detailed information on specific products (e.g., “Steel Frames for Residential Construction”):
Features: Highlight specific features like durability, eco-friendliness, precision, etc.
Technical Specs: Material grades, dimensions, finishes available.
Case Studies: A couple of client testimonials or case studies of where this product was used.
Downloadable Resources:

Technical datasheets or catalogs for users to download.
Include a form to capture user information before they download the document (optional for lead generation).
3. Projects/Portfolio Page
Gallery of Projects:
Display completed projects with high-quality images, each linked to a project detail page.
Filter options (e.g., industrial, residential, commercial).
Project Detail Pages:
A detailed description of the project, challenges, and how the steel frames were used.
other website we liked are:
https://www.tarnwickbuilds.example/
https://orlenbayhomes.example/

1. Objective:
Create an informative, professional, and visually appealing website that promotes steel frame construction solutions, showcasing the company’s offerings, expertise, and projects.
The website should highlight the benefits of steel frames (e.g., durability, sustainability, and cost-efficiency) and cater to both B2B and B2C clients.
2. Target Audience:
Primary: Architects, builders, and construction companies.
Secondary: Homeowners, investors, and property developers looking for modern, durable construction solutions.

```html
<!DOCTYPE html>
<html lang="en">
<head>
<meta charset="utf-8">
<title>Tarnwick – Steel Frame Construction</title>
<link href="https://fonts.googleapis.com/css2?family=Roboto:ital,wght@0,400;0,500;0,700;0,900;1,400&display=swap" rel="stylesheet">
<style>
:root{
  --blue:#1b72c0;
  --blue-dark:#155e9f;
  --grey-box:#b3b3b3;
  --ink:#333;
  --muted:#666;
  --light:#efefef;
  --footer:#333;
  --white:#fff;
}
*{box-sizing:border-box;margin:0;padding:0}
html,body{width:1200px;height:4749px;overflow:hidden}
body{font-family:'Roboto',sans-serif;color:var(--ink);background:var(--white);position:relative}
.abs{position:absolute}
.ph{position:absolute}
.pill{display:inline-flex;align-items:center;justify-content:center;border-radius:30px;font-weight:700;text-transform:uppercase;font-size:12px;letter-spacing:.3px}
.pill.outline{border:2px solid var(--white);color:var(--white)}
.pill.solid{background:var(--blue);color:var(--white)}

/* header */
.site-header{top:0;left:0;width:1200px;height:92px;border-top:4px solid var(--blue);background:#fff}
.brand{left:112px;top:28px;display:flex;align-items:center;gap:10px}
.brand-mark{width:34px;height:34px;background:var(--blue)}
.brand-name{font-size:34px;font-weight:700;color:var(--blue)}
.main-nav{right:112px;top:38px;display:flex;gap:26px;font-size:15px;text-transform:uppercase}
.main-nav a{color:var(--ink);text-decoration:none}
.main-nav a.active{color:var(--blue)}

/* hero */
.hero{top:92px;left:0;width:1200px;height:564px;background:linear-gradient(180deg,#5b6f80 0%,#8a98a4 35%,#6a6f72 70%,#4a4d50 100%)}
.hero-title{top:278px;width:1200px;text-align:center;color:#fff;font-size:38px;font-weight:500;text-shadow:0 2px 6px rgba(0,0,0,.4)}
.hero .pill{left:512px;top:346px;width:176px;height:46px;font-size:14px}

/* categories */
.categories{top:656px;left:0;width:1200px;height:275px;display:flex}
.cat{width:400px;height:275px;background:var(--blue);color:#fff;text-align:center;position:relative}
.cat.alt{background:var(--grey-box)}
.cat-icon{width:106px;height:106px;border-radius:50%;border:3px solid #fff;margin:24px auto 0;display:flex;align-items:center;justify-content:center;background:rgba(255,255,255,.1)}
.cat h3{font-size:18px;font-weight:500;margin-top:10px;text-transform:uppercase}
.cat p{font-size:11.5px;line-height:18px;width:300px;margin:4px auto 0}
.cat .pill{width:120px;height:37px;margin-top:14px;font-size:10.5px;font-weight:500}

/* welcome */
.welcome{top:931px;left:0;width:1200px;height:673px}
.framed{border:4px solid #fff;box-shadow:0 2px 6px rgba(0,0,0,.25)}
.eyebrow{font-size:23px;color:var(--muted);text-transform:uppercase;letter-spacing:.5px}
.big-title{font-size:46px;font-weight:900;color:var(--blue);text-transform:uppercase;line-height:1.05}
.body-copy{font-size:11.5px;line-height:18px;color:#444;text-align:justify}
.body-copy p+p{margin-top:12px}
.skyline{left:0;width:1200px;background:linear-gradient(180deg,rgba(220,225,230,.0),rgba(220,225,230,.7))}
.call{display:flex;align-items:center;gap:12px}
.call-icon{width:52px;height:52px;border-radius:50%;background:#ccc;display:flex;align-items:center;justify-content:center}
.call small{display:block;font-size:11px;color:#aaa;text-transform:uppercase}
.call strong{font-size:19px;font-weight:700;color:#222}

/* featured */
.featured{top:1604px;left:0;width:1200px;height:546px;background:var(--blue);color:#fff}
.section-title{width:1200px;text-align:center;font-size:38px;font-weight:900;text-transform:uppercase}
.proj{width:316px;top:138px;text-align:center}
.proj .img{height:230px;position:relative}
.proj p{font-size:12px;line-height:19px;margin-top:12px;padding:0 20px}

/* services */
.services{top:2150px;left:0;width:1200px;height:698px}
.svc{width:315px;height:232px}
.svc .img{height:187px;position:relative}
.svc .label{height:45px;background:var(--blue);color:#fff;font-size:15px;font-weight:700;display:flex;align-items:center;justify-content:center}

/* testimonial */
.testimonial{top:2848px;left:0;width:1200px;height:428px;background:var(--light)}
.avatar{border:5px solid #fff;box-shadow:0 3px 8px rgba(0,0,0,.25);background:linear-gradient(135deg,#b9c3cc,#6e7a86)}
.stars{top:112px;width:1200px;text-align:center}
.quote{top:158px;left:265px;width:670px;text-align:center;font-style:italic;font-size:13.5px;line-height:21px;color:#555}
.arrow-btn{width:34px;height:30px;border:2px solid var(--blue);display:flex;align-items:center;justify-content:center;background:#fff}
.arrow-btn.filled{background:var(--blue)}

/* partners */
.partner{width:183px;height:105px;border:1px solid #ddd;display:flex;align-items:center;justify-content:center;background:#fff}

/* contact */
.contact-band{top:4258px;left:0;width:1200px;height:415px;background:var(--blue);color:#fff}
.contact-info h2{font-size:32px;font-weight:900;text-transform:uppercase}
.info-row{display:flex;gap:10px;font-size:13px;line-height:21px;margin-top:18px}
.socials{display:flex;gap:9px;margin-top:26px}
.social{width:38px;height:38px;border:2px solid #fff;border-radius:50%}
.form-card{top:4145px;left:566px;width:522px;height:480px;background:#fff;box-shadow:0 2px 14px rgba(0,0,0,.15);padding:50px 38px 0}
.form-card h2{text-align:center;font-size:38px;font-weight:700;color:var(--ink);text-transform:uppercase;margin-bottom:22px}
.field{height:44px;border:1px solid #e4e8ec;background:#f5f7fa;font-size:12px;color:#777;padding:0 18px;display:flex;align-items:center;justify-content:space-between;margin-bottom:11px}
.field.area{height:104px;align-items:flex-start;padding-top:14px}
.submit{width:180px;height:54px;margin:26px auto 0;border-radius:30px;background:#222;color:#fff;font-weight:700;font-size:16px;display:flex;align-items:center;justify-content:center;text-transform:uppercase}
.site-footer{top:4673px;left:0;width:1200px;height:76px;background:var(--footer);color:#ddd;font-size:12px;display:flex;align-items:center;justify-content:center;text-transform:uppercase}
</style>
</head>
<body>

<header class="abs site-header">
  <div class="abs brand"><span class="brand-mark"></span><span class="brand-name">Tarnwick</span></div>
  <nav class="abs main-nav"><a class="active" href="#">Home</a><a href="#">About</a><a href="#">Products</a><a href="#">Services</a><a href="#">Contact Us</a></nav>
</header>

<section class="abs hero" role="img" aria-label="Interior of a large steel-framed industrial warehouse with stacked steel sections on the floor">
  <h1 class="abs hero-title">Strong Structures for Tomorrow</h1>
  <a class="abs pill outline">Get a Quote</a>
</section>

<section class="abs categories">
  <div class="cat">
    <div class="cat-icon"><svg width="56" height="56" viewBox="0 0 56 56" fill="none" stroke="#fff" stroke-width="2.5"><circle cx="18" cy="36" r="10"/><circle cx="32" cy="24" r="10"/><circle cx="42" cy="14" r="8"/></svg></div>
    <h3>Industrial</h3>
    <p>Lorem Ipsum is simply dummy text of the printing unknown printer galley make specimen book.</p>
    <a class="pill outline">Learn More</a>
  </div>
  <div class="cat alt">
    <div class="cat-icon"><svg width="56" height="56" viewBox="0 0 56 56" fill="none" stroke="#fff" stroke-width="2.5"><path d="M28 6 46 16v24L28 50 10 40V16z"/><path d="M28 6v44M10 16l18 10 18-10"/></svg></div>
    <h3>Residential</h3>
    <p>Lorem Ipsum is simply dummy text of the printing unknown printer galley make specimen book.</p>
    <a class="pill outline">Learn More</a>
  </div>
  <div class="cat">
    <div class="cat-icon"><svg width="56" height="56" viewBox="0 0 56 56" fill="none" stroke="#fff" stroke-width="2.5"><rect x="8" y="8" width="40" height="40" rx="6"/><circle cx="19" cy="19" r="3"/><circle cx="37" cy="37" r="3"/><rect x="26" y="24" width="12" height="8"/></svg></div>
    <h3>Commercial</h3>
    <p>Lorem Ipsum is simply dummy text of the printing unknown printer galley make specimen book.</p>
    <a class="pill outline">Learn More</a>
  </div>
</section>

<section class="abs welcome">
  <div class="ph" style="left:140px;top:80px;width:414px;height:450px;background:linear-gradient(180deg,#2e6fd0 0%,#5c6f82 45%,#9aa3aa 100%)" role="img" aria-label="Steel frame building under construction with steel beams stacked in front"></div>
  <div class="ph framed" style="left:112px;top:60px;width:122px;height:106px;background:linear-gradient(135deg,#9fb9d0,#3f6a92)" role="img" aria-label="Close-up of steel pipes"></div>
  <div class="ph framed" style="left:346px;top:386px;width:234px;height:160px;background:linear-gradient(135deg,#c9ced3,#6b7178)" role="img" aria-label="Stacked galvanised steel profiles"></div>
  <div class="abs" style="left:618px;top:72px;width:470px">
    <div class="eyebrow">Welcome to</div>
    <div class="big-title">Tarnwick</div>
    <div class="body-copy" style="margin-top:14px">
      <p>Lorem Ipsum is simply dummy text of the printing and typesetting industry. Lorem Ipsum has been the industry's standard dummy text ever since the 1500s, when an unknown printer took a galley of type and scrambled it to make a type specimen book. It has survived not only five centuries, but also the leap into electronic typesetting, remaining essentially unchanged. It was popularised in the 1960s with the release of Velmark sheets containing Lorem Ipsum passages, and more recently with desktop publishing software like Quillpage Studio including versions of Lorem Ipsum. Lorem Ipsum is simply dummy text of the printing and typesetting industry. Lorem Ipsum has publishing software like Quillpage Studio including versions of Lorem Ipsum.</p>
      <p>Lorem Ipsum is simply dummy text of the printing and typesetting industry. Lorem Ipsum has been the industry's standard dummy text ever since the 1500s, when an unknown printer took a galley of type and scrambled it to make a type specimen book. It has survived not only five centuries, but also the leap into electronic typesetting, remaining essentially unchanged. It was popularised in the 1960s with the release of Velmark sheets containing Lorem Ipsum passages, and more recently with desktop publishing software like Quillpage Studio including versions of Lorem Ipsum.</p>
    </div>
  </div>
  <a class="abs pill solid" style="left:623px;top:482px;width:183px;height:54px;font-size:13px">Learn More ›</a>
  <div class="abs call" style="left:828px;top:483px">
    <div class="call-icon"><svg width="22" height="22" viewBox="0 0 24 24" fill="#fff"><path d="M6.6 10.8a15 15 0 0 0 6.6 6.6l2.2-2.2c.3-.3.7-.4 1-.2 1.1.4 2.3.6 3.6.6.6 0 1 .4 1 1V20c0 .6-.4 1-1 1A17 17 0 0 1 3 4c0-.6.4-1 1-1h3.5c.6 0 1 .4 1 1 0 1.3.2 2.5.6 3.6.1.3 0 .7-.2 1z"/></svg></div>
    <div><small>Call anytime 24/7</small><strong>555-014-2290</strong></div>
  </div>
  <div class="abs skyline" style="top:571px;height:102px" role="img" aria-label="Faint city skyline silhouette"></div>
</section>

<section class="abs featured">
  <h2 class="abs section-title" style="top:52px">Featured Projects</h2>
  <div class="abs proj" style="left:112px"><div class="img" style="background:linear-gradient(135deg,#d7dbdf,#7b8288)" role="img" aria-label="Stacked square steel tubing"></div><p>Lorem Ipsum is simply dummy text of the printing unknown printer galley make specimen book.</p></div>
  <div class="abs proj" style="left:442px"><div class="img" style="background:linear-gradient(180deg,#3d5a8a,#a4473a 55%,#3a3f47)" role="img" aria-label="Steel mill interior with large pipes"></div><p>Lorem Ipsum is simply dummy text of the printing unknown printer galley make specimen book.</p></div>
  <div class="abs proj" style="left:772px"><div class="img" style="background:linear-gradient(135deg,#e9eef3,#5b7490 60%,#2c3a4a)" role="img" aria-label="Stack of large steel pipes"></div><p>Lorem Ipsum is simply dummy text of the printing unknown printer galley make specimen book.</p></div>
  <a class="abs pill outline" style="left:502px;top:446px;width:196px;height:50px">View All Projects</a>
</section>

<section class="abs services">
  <h2 class="abs section-title" style="top:50px;color:var(--ink)">Our Services</h2>
  <div class="abs svc" style="left:112px;top:134px"><div class="img" style="background:linear-gradient(180deg,#a9c3dd,#6d7b88)" role="img" aria-label="Steel wall framing against the sky"></div><div class="label">Wall Framing</div></div>
  <div class="abs svc" style="left:443px;top:134px"><div class="img" style="background:linear-gradient(180deg,#8fa7bd,#5c6b76)" role="img" aria-label="Steel roof trusses inside a warehouse"></div><div class="label">Roof Trusses</div></div>
  <div class="abs svc" style="left:773px;top:134px"><div class="img" style="background:linear-gradient(180deg,#c6ccd1,#5f6a73)" role="img" aria-label="Stacked steel beams"></div><div class="label">WIDESPAN</div></div>
  <div class="abs svc" style="left:112px;top:382px"><div class="img" style="background:linear-gradient(135deg,#e8d3a8,#8a6a3c)" role="img" aria-label="Glass and steel façade framing"></div><div class="label">Façade framing</div></div>
  <div class="abs svc" style="left:443px;top:382px"><div class="img" style="background:linear-gradient(180deg,#cfdbe6,#7d8e9c)" role="img" aria-label="Row of steel storage silos"></div><div class="label">Transportable Buildings</div></div>
  <div class="abs svc" style="left:773px;top:382px"><div class="img" style="background:linear-gradient(180deg,#a4b4c4,#5e7268)" role="img" aria-label="Residential houses with steel frames and scaffolding"></div><div class="label">Residential</div></div>
</section>

<section class="abs testimonial">
  <div class="ph avatar" style="left:70px;top:12px;width:130px;height:110px;transform:rotate(-12deg)" role="img" aria-label="Portrait of a smiling client"></div>
  <div class="ph avatar" style="left:970px;top:2px;width:118px;height:120px;transform:rotate(8deg)" role="img" aria-label="Portrait of an older client"></div>
  <div class="ph avatar" style="left:168px;top:295px;width:130px;height:118px;transform:rotate(-10deg)" role="img" aria-label="Portrait of a client"></div>
  <div class="ph avatar" style="left:842px;top:292px;width:138px;height:122px;transform:rotate(8deg)" role="img" aria-label="Portrait of a client at a laptop"></div>
  <h2 class="abs section-title" style="top:50px;font-size:40px;color:var(--ink);font-weight:700">Testimonial</h2>
  <div class="abs stars"><svg width="112" height="20" viewBox="0 0 112 20"><g fill="#f5b400" stroke="#f5b400"><path id="st" d="M10 1l2.6 5.6 6 .7-4.5 4.1 1.2 6L10 14.4 4.7 17.4l1.2-6L1.4 7.3l6-.7z"/><use href="#st" x="22"/><use href="#st" x="44"/><use href="#st" x="66"/></g><use href="#st" x="88" fill="none" stroke="#f5b400"/></svg></div>
  <p class="abs quote">Lorem Ipsum is simply dummy text of the printing and typesetting industry. Lorem Ipsum has been the industry's standard dummy text ever since the 1500s, when an unknown printer took a galley of type and scrambled it to make type specimen book. It has survived not only five centuries, but also the leap into electronic typesetting, remaining essentially unchanged. of Velmark sheets containing Lorem Ipsum passages, and more recently with desktop publishing software like Quillpage</p>
  <div class="abs arrow-btn" style="left:206px;top:185px"><svg width="10" height="12" viewBox="0 0 10 12" fill="none" stroke="#1b72c0" stroke-width="2"><path d="M7 1 2 6l5 5"/></svg></div>
  <div class="abs arrow-btn filled" style="left:954px;top:185px"><svg width="10" height="12" viewBox="0 0 10 12" fill="none" stroke="#fff" stroke-width="2"><path d="M3 1l5 5-5 5"/></svg></div>
  <div class="abs" style="top:300px;width:1200px;text-align:center;font-size:17px;font-weight:500">Marcus Hale</div>
  <div class="abs" style="top:322px;width:1200px;text-align:center;font-size:14px;color:#999">Director</div>
</section>

<section class="abs" style="top:3276px;left:0;width:1200px;height:586px">
  <div class="abs" style="left:112px;top:100px;width:468px">
    <div class="eyebrow">Why Choose</div>
    <div class="big-title">Tarnwick</div>
    <div class="body-copy" style="margin-top:14px">
      <p>Lorem Ipsum is simply dummy text of the printing and typesetting industry. Lorem Ipsum has been the industry's standard dummy text ever since the 1500s, when an unknown printer took a galley of type and scrambled it to make a type specimen book. It has survived not only five centuries, but also the leap into electronic typesetting, remaining essentially unchanged. It was popularised in the 1960s with the release of Velmark simply dummy text of the printing and typesetting industry. Lorem Ipsum has been publishing software like Quillpage Studio including versions of Lorem Ipsum.</p>
      <p>Lorem Ipsum is simply dummy text of the printing and typesetting industry. Lorem Ipsum has been the industry's standard dummy text ever since the 1500s, when an unknown printer took a galley of type and scrambled it to make a type specimen book. It has survived not only five centuries, but also the leap into electronic typesetting, remaining essentially unchanged. It was popularised in the 1960s with the release of Velmark sheets containing Lorem Ipsum passages, and more recently with desktop publishing software like Quillpage Studio including versions of Lorem Ipsum.</p>
    </div>
  </div>
  <a class="abs pill solid" style="left:112px;top:486px;width:184px;height:54px;font-size:13px">Get a Quote ›</a>
  <div class="ph" style="left:651px;top:90px;width:414px;height:448px;background:linear-gradient(180deg,#2e6fd0 0%,#5c6f82 45%,#9aa3aa 100%)" role="img" aria-label="Steel frame building under construction"></div>
  <div class="ph framed" style="left:622px;top:62px;width:124px;height:108px;background:linear-gradient(135deg,#d5d9dd,#6a7178)" role="img" aria-label="Close-up of steel tube ends"></div>
  <div class="ph framed" style="left:856px;top:392px;width:234px;height:160px;background:linear-gradient(135deg,#bcd0e2,#5f7184)" role="img" aria-label="Steel roof framing against the sky"></div>
</section>

<section class="abs" style="top:3862px;left:0;width:1200px;height:268px">
  <h2 class="abs section-title" style="top:32px;font-size:30px;color:var(--ink);font-weight:700">Partnerships</h2>
  <div class="abs" style="left:112px;top:100px;display:flex;gap:15px">
    <div class="partner"><span style="width:60px;height:60px;border-radius:50%;background:#444;display:block"></span></div>
    <div class="partner"><span style="width:60px;height:60px;background:var(--blue);display:block"></span></div>
    <div class="partner"><span style="width:60px;height:60px;background:#555;display:block"></span></div>
    <div class="partner"><span style="width:60px;height:60px;border-radius:50%;background:#3a9b3a;display:block"></span></div>
    <div class="partner"><span style="width:60px;height:60px;background:#1a4fa3;display:block"></span></div>
  </div>
</section>

<div class="abs skyline" style="top:4130px;height:128px" role="img" aria-label="Faint city skyline silhouette"></div>
<section class="abs contact-band">
  <div class="abs contact-info" style="left:112px;top:52px">
    <h2>Contact Info</h2>
    <div class="info-row"><svg width="12" height="16" viewBox="0 0 12 16" fill="#fff"><path d="M6 0a6 6 0 0 0-6 6c0 4.5 6 10 6 10s6-5.5 6-10a6 6 0 0 0-6-6zm0 8.5A2.5 2.5 0 1 1 6 3.5a2.5 2.5 0 0 1 0 5z"/></svg><span>Lorem Ipsum is simply dummy text<br>the printing and typesetting industry.</span></div>
    <div class="info-row"><svg width="14" height="12" viewBox="0 0 14 12" fill="none" stroke="#fff" stroke-width="1.4"><rect x=".7" y=".7" width="12.6" height="10.6"/><path d="M1 1l6 5 6-5"/></svg><span>info@tarnwick.example</span></div>
    <div class="info-row"><svg width="13" height="13" viewBox="0 0 24 24" fill="#fff"><path d="M6.6 10.8a15 15 0 0 0 6.6 6.6l2.2-2.2c.3-.3.7-.4 1-.2 1.1.4 2.3.6 3.6.6.6 0 1 .4 1 1V20c0 .6-.4 1-1 1A17 17 0 0 1 3 4c0-.6.4-1 1-1h3.5c.6 0 1 .4 1 1 0 1.3.2 2.5.6 3.6.1.3 0 .7-.2 1z"/></svg><span>555-014-2290</span></div>
    <div class="socials"><span class="social"></span><span class="social"></span><span class="social"></span><span class="social"></span></div>
  </div>
</section>
<form class="abs form-card">
  <h2>Get in Touch</h2>
  <div class="field">Enter your name</div>
  <div class="field">Enter your email</div>
  <div class="field">Date <svg width="14" height="14" viewBox="0 0 14 14" fill="none" stroke="#999"><rect x="1" y="2.5" width="12" height="10.5"/><path d="M1 5.5h12M4 1v3M10 1v3"/></svg></div>
  <div class="field area">Enter your message</div>
  <div class="submit">Submit Now</div>
</form>

<footer class="abs site-footer">Copyright © 2024 tarnwick.example. All rights reserved</footer>

</body>
</html>
```